高単価、会員制の予備校になります。
定員MAX20名。
浪人生には受験職人が担任となり、授業だけでなく普段の自習や生活態度の面倒を見て合格を目指していきます。
高校生には学校が終わった後の生活の学習の面倒を見ていきます。

「高級感」「独自性」「受験職人」

がキーワードだと思っています。
1.大学受験コンサルティング
2.医学部/難関大学専門
3.会社のロゴを入れる(少しアレンジして高級感を出すとより良い)

サイズ(横:縦=500mm:2000mm)多少の変更があっても問題無いです。
赤系、赤、白、黒(少し)
今会社で使用しているロゴを添付しています。
壁看板に塾名は入れるので今回の看板に塾名は入れなくても良いです。
ロゴは入れて欲しいです。

一番初めのデザインが良かったのと、その後の細かい修正点などを丁寧に対応していただいた点で選びました。

今回提案して頂いてありがとうございました。
看板のデザインを考えながら「魅せ方」をいろいろ考える事ができたので勉強になりました。
またお願いすると思いますのでその時もよろしくお願いいたします。

```html
<!DOCTYPE html>
<html lang="ja">
<head>
<meta charset="UTF-8">
<title>大学受験コンサルティング 縦看板</title>
<link rel="stylesheet" href="https://fonts.googleapis.com/css2?family=Yuji+Syuku&display=swap">
<style>
  :root {
    --sign-red: #c00019;
    --sign-red-dark: #8e0010;
    --glow-red: rgba(200, 0, 25, 0.45);
    --paper: #ffffff;
  }
  html, body {
    margin: 0;
    padding: 0;
    width: 1200px;
    height: 4812px;
    overflow: hidden;
    background: var(--paper);
  }
  .banner {
    position: relative;
    width: 1200px;
    height: 4812px;
    background: var(--paper);
    font-family: "Yuji Syuku", serif;
    color: var(--sign-red);
  }
  .tagline {
    position: absolute;
    margin: 0;
    writing-mode: vertical-rl;
    text-orientation: upright;
    font-weight: 400;
    font-size: 220px;
    line-height: 1;
    letter-spacing: 36px;
    text-shadow: 0 0 14px var(--glow-red), 0 0 28px var(--glow-red);
    white-space: nowrap;
  }
  .tagline--service {
    left: 630px;
    top: 236px;
  }
  .tagline--specialty {
    left: 270px;
    top: 256px;
  }
  .brand {
    position: absolute;
    left: 0;
    top: 3640px;
    width: 1200px;
    display: flex;
    flex-direction: column;
    align-items: center;
    gap: 90px;
  }
  .brand__square {
    width: 300px;
    height: 300px;
    background: var(--sign-red);
  }
  .brand__name {
    margin: 0;
    font-size: 200px;
    line-height: 1;
    letter-spacing: 20px;
    color: var(--sign-red);
  }
</style>
</head>
<body>
  <main class="banner">
    <h1 class="tagline tagline--service">大学受験コンサルティング</h1>
    <p class="tagline tagline--specialty">医学部／難関大学専門</p>
    <div class="brand">
      <div class="brand__square" aria-hidden="true"></div>
      <p class="brand__name">紅誠ゼミ</p>
    </div>
  </main>
</body>
</html>
```